Fun Veterinary Marketing Graphic for branding

Looking to add a graphic that explains each word ( Come Sit Heal) in picture. Maybe three squares with the graphic inside and the word below the graphic. This graphic will be used for a veterinary office to in courage to come to our office, sit be comfy, let us care or heal your pet.

We would like to see the use of dogs and cats in the illustrations
Updates

A better explanation of what I am looking for is as follow.

Look at it as creating a story board for the words Come Sit Heal. With the story above each word. Looking for something can’t translate well to marketing goods as well as promotional items.

Target Market(s)

Pet owners

Industry/Entity Type

Veterinary

Requirements
Must have
• An image for each work Come. Sit. Heal
Nice to have
• Our hospital name possibly added in Brindlecroft Animal Clinic one with it and one without

```html
<!DOCTYPE html>
<html lang="en">
<head>
<meta charset="utf-8">
<title>Brindlecroft Animal Clinic — Come, Sit, Heal</title>
<link rel="stylesheet" href="https://fonts.googleapis.com/css2?family=Arimo:wght@700&family=Montserrat:wght@500&display=swap">
<style>
  :root {
    --frame: #b3b3b3;
    --sunflower: #fda916;
    --meadow: #37cb67;
    --periwinkle: #6666ff;
    --sky-heart: #6699ff;
    --navy-slate: #485aa8;
    --tangerine: #ff6a00;
    --deep-teal: #003330;
    --ink: #111111;
    --cream: #f5efe2;
    --white: #ffffff;
    --coral: #f08a78;
  }
  html, body {
    margin: 0;
    padding: 0;
    width: 1200px;
    height: 851px;
    overflow: hidden;
    background: var(--frame);
  }
  .poster {
    display: block;
    width: 1200px;
    height: 851px;
  }
  .clinic-name {
    font-family: "Montserrat", sans-serif;
    font-weight: 500;
    font-size: 22px;
    letter-spacing: 15.5px;
    fill: var(--ink);
  }
  .story-word {
    font-family: "Arimo", Arial, sans-serif;
    font-weight: 700;
    font-size: 88px;
    fill: var(--white);
  }
  .ring { fill: none; stroke-width: 4; }
  .ring--ink { stroke: var(--ink); }
  .ring--sun { stroke: var(--sunflower); }
  .line-icon { fill: none; stroke-linecap: round; stroke-linejoin: round; }
</style>
</head>
<body>
<svg class="poster" viewBox="0 0 1200 851" xmlns="http://www.w3.org/2000/svg">
  <defs>
    <linearGradient id="tabby-tones" x1="0" y1="0" x2="1" y2="1">
      <stop offset="0" stop-color="#8a8680"/>
      <stop offset="1" stop-color="#4a4743"/>
    </linearGradient>
    <linearGradient id="pug-tones" x1="0" y1="0" x2="0" y2="1">
      <stop offset="0" stop-color="#c7a98a"/>
      <stop offset="1" stop-color="#e8dcc8"/>
    </linearGradient>
    <linearGradient id="vet-tones" x1="0" y1="0" x2="1" y2="0">
      <stop offset="0" stop-color="#b57645"/>
      <stop offset="1" stop-color="#dedede"/>
    </linearGradient>
  </defs>

  <!-- Story panels -->
  <g class="panels">
    <rect class="panel panel--come" x="22" y="14" width="387" height="821" fill="var(--sunflower)"/>
    <rect class="panel panel--sit" x="409" y="14" width="370" height="821" fill="var(--meadow)"/>
    <rect class="panel panel--heal" x="779" y="14" width="396" height="821" fill="var(--periwinkle)"/>
  </g>

  <text class="clinic-name" x="285" y="93">BRINDLECROFT ANIMAL CLINIC</text>

  <!-- COME -->
  <g class="story story--come">
    <path class="backdrop" d="M113 190 H250 A67 67 0 0 1 317 257 V396 H113 Z" fill="var(--white)"/>
    <path class="quadrant quadrant--paw" d="M113 396 H215 V498 A102 102 0 0 1 113 396 Z" fill="var(--tangerine)"/>
    <path class="quadrant quadrant--bone" d="M215 396 H317 A102 102 0 0 1 215 498 Z" fill="var(--navy-slate)"/>
    <rect class="photo photo--kitten" x="128" y="157" width="252" height="239" rx="60" fill="url(#tabby-tones)" role="img" aria-label="Photo of a tabby kitten raising one paw to wave"/>
    <g class="ball">
      <circle cx="115" cy="390" r="38" fill="var(--ink)"/>
      <path d="M77 390 H153" stroke="var(--cream)" stroke-width="3" fill="none"/>
      <path d="M115 352 A30 30 0 0 0 150 380" stroke="var(--cream)" stroke-width="3" fill="none"/>
      <path d="M110 428 A30 30 0 0 0 84 402" stroke="var(--cream)" stroke-width="3" fill="none"/>
    </g>
    <g class="icon icon--paw line-icon" stroke="var(--ink)" stroke-width="2">
      <ellipse cx="166" cy="446" rx="8" ry="7"/>
      <circle cx="158" cy="429" r="3.5"/>
      <circle cx="168" cy="425" r="3.5"/>
      <circle cx="178" cy="430" r="3.5"/>
      <circle cx="182" cy="441" r="3.5"/>
    </g>
    <g class="icon icon--bone line-icon" stroke="var(--white)" stroke-width="3">
      <path d="M244 430 L272 420 M244 430 A5 5 0 1 1 238 440 A5 5 0 1 1 244 452 L272 420 A5 5 0 1 1 280 416 A5 5 0 1 1 282 426 Z"/>
    </g>
    <ellipse class="ring ring--ink" cx="217" cy="563" rx="139" ry="24" transform="rotate(-5 217 563)"/>
    <text class="story-word" x="86" y="592">Come</text>
    <path class="paw-wave" d="M22 790 L80 730 L110 745 L110 760 L22 835 Z" fill="var(--white)" role="img" aria-label="Illustration of a white cartoon cat paw reaching in from the corner"/>
  </g>

  <!-- SIT -->
  <g class="story story--sit">
    <path class="backdrop" d="M696 338 V536 H498 A198 198 0 0 1 696 338 Z" fill="var(--sunflower)"/>
    <path class="quadrant quadrant--yarn" d="M498 536 H596 V635 A99 99 0 0 1 498 536 Z" fill="var(--ink)"/>
    <path class="quadrant quadrant--paw" d="M596 536 H695 A99 99 0 0 1 596 635 Z" fill="var(--deep-teal)"/>
    <rect class="photo photo--pug" x="516" y="270" width="170" height="267" rx="70" fill="url(#pug-tones)" role="img" aria-label="Photo of a fawn pug sitting with its tongue out"/>
    <g class="icon icon--yarn line-icon" stroke="var(--cream)" stroke-width="2">
      <circle cx="558" cy="584" r="22"/>
      <path d="M540 572 L572 600 M546 566 L578 592 M538 582 L562 604"/>
      <path d="M536 584 C528 560 540 548 548 556"/>
    </g>
    <g class="icon icon--paw" fill="var(--sunflower)">
      <ellipse cx="637" cy="587" rx="8" ry="7"/>
      <circle cx="627" cy="574" r="3.5"/>
      <circle cx="635" cy="568" r="3.5"/>
      <circle cx="644" cy="570" r="3.5"/>
      <circle cx="649" cy="579" r="3.5"/>
    </g>
    <ellipse class="ring ring--sun" cx="600" cy="215" rx="139" ry="40" transform="rotate(-6 600 215)"/>
    <text class="story-word" x="544" y="248">Sit</text>
    <path class="corner corner--sit" d="M685 741 H779 V835 A94 94 0 0 1 685 741 Z" fill="var(--periwinkle)"/>
    <path class="line-icon" d="M738 768 V788 M728 778 H748" stroke="var(--white)" stroke-width="5"/>
  </g>

  <!-- HEAL -->
  <g class="story story--heal">
    <path class="heart" d="M976 427 L870 320 A60 60 0 0 1 976 250 A60 60 0 0 1 1088 320 Z" fill="var(--sky-heart)"/>
    <ellipse class="ring ring--ink" cx="977" cy="313" rx="139" ry="40" transform="rotate(-5 977 313)"/>
    <text class="story-word" x="882" y="346">Heal</text>
    <path class="corner corner--heal" d="M1097 126 H1175 V203 A78 78 0 0 1 1097 126 Z" fill="var(--navy-slate)"/>
    <g class="icon icon--syringe line-icon" stroke="var(--white)" stroke-width="2">
      <path d="M1122 138 L1158 174 M1128 152 L1144 136 M1134 158 L1150 142 M1142 166 L1158 150"/>
      <circle cx="1148" cy="148" r="7"/>
      <path d="M1148 144 V152 M1144 148 H1152"/>
    </g>
    <rect class="illustration illustration--vet" x="802" y="445" width="373" height="390" rx="40" fill="url(#vet-tones)" role="img" aria-label="Illustration of a veterinarian in a white coat listening to a brown dog with a stethoscope"/>
  </g>

  <!-- Confetti -->
  <g class="confetti line-icon">
    <path d="M321 178 V202 M309 190 H333" stroke="var(--white)" stroke-width="5"/>
    <path d="M316 484 V496 M310 490 H322" stroke="var(--white)" stroke-width="3"/>
    <path d="M1118 80 V94 M1111 87 H1125" stroke="var(--navy-slate)" stroke-width="4"/>
    <circle cx="108" cy="486" r="8" stroke="var(--white)" stroke-width="4"/>
    <circle cx="332" cy="702" r="8" stroke="var(--tangerine)" stroke-width="4"/>
    <circle cx="503" cy="570" r="8" stroke="var(--coral)" stroke-width="4"/>
    <path d="M413 396 C396 410 400 420 408 428 C416 436 416 446 404 456 C394 466 400 476 408 484 C414 490 410 496 400 494" stroke="var(--cream)" stroke-width="5"/>
    <path d="M750 490 C760 496 770 488 772 476 C774 466 782 460 788 468 C794 474 796 454 802 452" stroke="var(--sunflower)" stroke-width="4"/>
    <path d="M676 382 A17 17 0 0 0 712 382" stroke="var(--navy-slate)" stroke-width="5"/>
    <path d="M864 596 A20 20 0 0 0 838 624" stroke="var(--white)" stroke-width="5"/>
  </g>
</svg>
</body>
</html>
```